Modern Billboard Ad for Criminal Defense Firm

10.5 x 36 We're looking for something to set us apart from the local competition. Looking for sleek and modern. We're a mid-sized firm in a small market city. We want to give the artist room to be creative on this one.
Thanks

Target Market(s)

Adult clients who have been charged with a crime/DWI

Industry/Entity Type

legal

Font styles to use
Serif
Sans Serif

Requirements
Must have
• Needs to have the firm name in large lettering. Law Offices of Marcus T Whitfield. “PLLC” does not have to be included. Phone number of (555) 384-1927 should be included but not the main focus.
Nice to have
• A call to action or something similar. “Don’t go it alone, call today.”, “ Arrested?”

```html
<!DOCTYPE html>
<html lang="en">
<head>
<meta charset="utf-8">
<title>Law Offices of Marcus T Whitfield — Billboard</title>
<link href="https://fonts.googleapis.com/css2?family=Arimo:wght@700&display=swap" rel="stylesheet">
<style>
  :root {
    --page-bg: #e9ecf1;
    --panel-top: #0f4d93;
    --panel-bottom: #0a1f4e;
    --photo-light: #9a9a9a;
    --photo-dark: #3a3a3a;
    --text: #ffffff;
    --badge-frame: #4aa8dc;
    --badge-body: #1c1c1c;
    --badge-band: #5fb6e4;
  }
  * { margin: 0; padding: 0; box-sizing: border-box; }
  html, body {
    width: 1200px; height: 1200px; overflow: hidden;
    background: var(--page-bg);
  }
  .canvas {
    width: 1200px; height: 1200px;
    display: flex; align-items: center; justify-content: center;
  }
  .billboard {
    position: relative;
    width: 1120px; height: 327px;
    background: linear-gradient(180deg, var(--panel-top) 0%, var(--panel-bottom) 100%);
    box-shadow: 0 18px 40px rgba(10, 31, 78, 0.25);
    font-family: 'Arimo', Arial, sans-serif;
    color: var(--text);
  }
  .attorney-photo {
    position: absolute; left: 36px; top: 34px;
    width: 248px; height: 260px;
    background: linear-gradient(135deg, var(--photo-light) 0%, #6b6b6b 50%, var(--photo-dark) 100%);
  }
  .firm-block {
    position: absolute; left: 300px; right: 130px; top: 0; bottom: 0;
    display: flex; flex-direction: column; align-items: center; justify-content: center;
    text-align: center;
  }
  .firm-intro { font-size: 40px; font-weight: 700; letter-spacing: 0.3px; margin-bottom: 14px; }
  .firm-name { font-size: 58px; font-weight: 700; letter-spacing: 0.5px; line-height: 1; margin-bottom: 22px; white-space: nowrap; }
  .firm-phone { display: flex; align-items: center; gap: 14px; font-size: 40px; font-weight: 700; }
  .firm-phone svg { width: 36px; height: 36px; }
  .award-badge {
    position: absolute; right: 24px; bottom: 20px;
    width: 90px; height: 148px;
    background: var(--badge-body);
    border: 4px solid var(--badge-frame);
  }
  .award-badge::before {
    content: ""; position: absolute; left: 0; right: 0; top: 0; height: 22px;
    background: var(--badge-band);
  }
  .award-badge::after {
    content: ""; position: absolute; left: 0; right: 0; bottom: 0; height: 24px;
    background: var(--badge-band);
  }
</style>
</head>
<body>
  <div class="canvas">
    <section class="billboard">
      <div class="attorney-photo" role="img" aria-label="Black and white portrait of the attorney in a vest and tie with a jacket over his shoulder"></div>
      <div class="firm-block">
        <p class="firm-intro">Law Offices of</p>
        <h1 class="firm-name">MARCUS T WHITFIELD</h1>
        <p class="firm-phone">
          <svg viewBox="0 0 24 24" aria-hidden="true"><path fill="#ffffff" d="M6.6 10.8c1.4 2.8 3.8 5.1 6.6 6.6l2.2-2.2c.3-.3.7-.4 1-.2 1.1.4 2.3.6 3.6.6.6 0 1 .4 1 1V20c0 .6-.4 1-1 1C10.6 21 3 13.4 3 4c0-.6.4-1 1-1h3.5c.6 0 1 .4 1 1 0 1.3.2 2.5.6 3.6.1.3 0 .7-.2 1L6.6 10.8z"/></svg>
          (555) 384-1927
        </p>
      </div>
      <div class="award-badge" role="img" aria-label="Community choice award badge"></div>
    </section>
  </div>
</body>
</html>
```